A combined poster for Martial arts club and Dance club.

We need a poster that will be hung opp and used in street bucks for advertisement. We are two independent clubs ( a dance studio and a MA gym) but have chosen to cooperate and split costs for advertisement. We also see an effect with both arts on the same poster.

We have a attached a picture with both arts doing a pose from each other. This would be great to use.

Target Market(s)

All ages primarily young people

Industry/Entity Type

Martial Art

Colors

Designer to choose colors to be used in the design.

Requirements
Must have
• A professional look. Both logos and either one of the attached pictures.
• Fight styles: Check webpage: http://www.brakvelhall.no
• Dance Styles: http://trinnlagetsalen7.com
• Contact information Address and phone
• Space for texts slogans.
Nice to have
• Photoshop the picture with different background or cut them out.

```html
<!DOCTYPE html>
<html lang="en">
<head>
<meta charset="utf-8">
<title>Brakvel Hall × Trinnlaget Salen 7 — Street Poster</title>
<link href="https://fonts.googleapis.com/css2?family=Teko:wght@700&family=Roboto:wght@400;700&display=swap" rel="stylesheet">
<style>
  :root {
    --page-bg: #e9edf1;
    --poster-light: #ffffff;
    --poster-cyan: #7fe0f7;
    --poster-blue: #1aa6e0;
    --poster-deep: #0f86c4;
    --photo-light: #f4f8fb;
    --photo-mid: #c9dbe6;
    --photo-warm: #e8d9c4;
    --photo-blue: #3b5fa6;
    --ink: #0c0c0c;
    --bar: #0b0b0b;
    --bar-text: #ffffff;
    --logo-blue: #1b5fa8;
  }
  * { margin: 0; padding: 0; box-sizing: border-box; }
  html, body { width: 1200px; height: 896px; overflow: hidden; }
  body {
    background: var(--page-bg);
    font-family: "Roboto", Arial, sans-serif;
    position: relative;
  }
  .poster {
    position: absolute;
    left: 356px; top: 18px;
    width: 488px; height: 860px;
    overflow: hidden;
    background:
      radial-gradient(ellipse at 52% 40%, var(--poster-light) 0%, var(--poster-cyan) 38%, var(--poster-blue) 78%, var(--poster-deep) 100%);
    box-shadow: 0 6px 24px rgba(0,0,0,.18);
  }
  .club-marks {
    position: absolute; top: 34px; left: 40px; right: 30px;
    display: flex; justify-content: space-between; align-items: center;
  }
  .club-mark {
    display: flex; align-items: center; gap: 7px;
    font-weight: 700; font-size: 16px; color: var(--ink);
    letter-spacing: .5px; line-height: 1;
  }
  .club-mark .dot {
    width: 28px; height: 28px; border-radius: 50%;
    background: var(--logo-blue);
  }
  .club-mark--dance .dot { background: var(--ink); border-radius: 0; width: 20px; height: 20px; }
  .hero-photo {
    position: absolute; left: 58px; top: 86px;
    width: 382px; height: 480px;
    border-radius: 10px;
    border: 2px solid rgba(255,255,255,.85);
    background:
      linear-gradient(100deg,
        var(--photo-light) 0%, var(--photo-mid) 30%, var(--photo-blue) 44%,
        var(--photo-mid) 52%, var(--photo-warm) 68%, var(--photo-light) 100%);
    opacity: .92;
    box-shadow: 0 8px 26px rgba(10,70,120,.25);
  }
  .slogan {
    position: absolute; left: 48px; top: 428px; width: 400px;
    font-family: "Teko", "Arial Narrow", sans-serif;
    font-weight: 700; color: var(--ink);
    font-size: 118px; line-height: .82;
    text-transform: uppercase; letter-spacing: 1px;
  }
  .slogan span { display: block; }
  .slogan .line-3 { text-align: right; }
  .contact-bar {
    position: absolute; left: 0; right: 0; bottom: 0; height: 84px;
    background: var(--bar); color: var(--bar-text);
    display: grid; grid-template-columns: 1fr 1.45fr;
    grid-template-rows: auto auto; align-content: center;
    padding: 0 22px 0 28px; row-gap: 14px;
    font-size: 13px;
  }
  .contact-item { display: flex; align-items: center; gap: 8px; white-space: nowrap; line-height: 1; }
  .contact-item.right { justify-content: flex-end; }
  .contact-item svg { width: 12px; height: 12px; fill: var(--bar-text); flex: none; }
</style>
</head>
<body>
  <article class="poster">
    <header class="club-marks">
      <div class="club-mark club-mark--martial"><span class="dot"></span>BRAKVEL HALL</div>
      <div class="club-mark club-mark--dance"><span class="dot"></span>TRINNLAGET SALEN 7</div>
    </header>

    <div class="hero-photo" role="img" aria-label="Photo: a martial artist in a white gi and a ballerina in a tutu, each striking the other's pose"></div>

    <h1 class="slogan">
      <span class="line-1">Your</span>
      <span class="line-2">Slogan</span>
      <span class="line-3">Here</span>
    </h1>

    <footer class="contact-bar">
      <div class="contact-item">
        <svg viewBox="0 0 24 24"><path d="M6.6 10.8a15 15 0 0 0 6.6 6.6l2.2-2.2a1 1 0 0 1 1-.25 11.4 11.4 0 0 0 3.6.57 1 1 0 0 1 1 1V20a1 1 0 0 1-1 1A17 17 0 0 1 3 4a1 1 0 0 1 1-1h3.5a1 1 0 0 1 1 1c0 1.25.2 2.450.57 3.57a1 1 0 0 1-.25 1z"/></svg>
        555-010-42-00
      </div>
      <div class="contact-item right">
        <svg viewBox="0 0 24 24"><path d="M12 2a7 7 0 0 0-7 7c0 5.25 7 13 7 13s7-7.75 7-13a7 7 0 0 0-7-7zm0 9.5A2.5 2.5 0 1 1 12 6.5a2.5 2.5 0 0 1 0 5z"/></svg>
        24 Larkfield Row, Eastbrook, QX4 2LM
      </div>
      <div class="contact-item">
        <svg viewBox="0 0 24 24"><path d="M2 5h20v14H2zm2 2v.5l8 5 8-5V7z"/></svg>
        info@brakvelhall.no
      </div>
      <div class="contact-item right">
        <svg viewBox="0 0 24 24"><circle cx="12" cy="12" r="9" fill="none" stroke="#fff" stroke-width="2"/><path d="M3 12h18M12 3c3 3 3 15 0 18M12 3c-3 3-3 15 0 18" fill="none" stroke="#fff" stroke-width="1.6"/></svg>
        www.brakvelhall.no
      </div>
    </footer>
  </article>
</body>
</html>
```